Brightmore Machinery Forklift rental website

I'm seeking a proficient web developer to build a forklift rental website tailored to large warehouses. I am not looking for a generic site, I want it to be attractive and sleek to potential customers. I have attached my logo to give a better idea about my design preferences .
The site must encompass various functionalities: - A rental booking system to allow customers reserve forklifts seamlessly, making the rental process simpler. - An inventory management system that offers real-time tracking of our diverse range of forklifts including Electric forklifts, Reach trucks, Order pickers, Sit and Stand up counterbalances, Swing reach, Propane sit down counterbalances and chargers. For each forklift listed, the site should display explicit specifications, current rental rates, and an availability calendar to aid customers in making informed rental decisions. Ideal skills for this role will include web development, experience in building booking and potentially some knowledge of the renting industry, although this is not essential. Experience in creating inventory management systems is also looked upon favorably. I would also like a section that I can list forklifts for sale. Preferably the website would be designed to convert into an app as well. The website will need a payment portal that can accept credit cards, ach payments and possibly e-check/ wire transfer.
Most bookings will be monthly so I need a system that can accommodate that. I will also need an option to leave the bookings open ended in the event the customer wants to keep the unit until further notice.
Target Market(s)
Industrial warehouses
Coding
Coded - Design and coding required
Number of Pages Required
1 page
Look and feel
Each slider illustrates characteristics of the customer's brand and the style your logo design should communicate.

```html
<!DOCTYPE html>
<html lang="en">
<head>
<meta charset="utf-8">
<title>Brightmore Machinery — Forklift Rental</title>
<link href="https://fonts.googleapis.com/css2?family=Barlow:wght@400;500;600;700&family=Russo+One&display=swap" rel="stylesheet">
<style>
:root{
  --red:#e31e24;
  --navy:#1e2b5c;
  --ink:#0d1230;
  --sale:#1f3479;
  --text:#222833;
  --muted:#5d6270;
  --line:#d9dbe1;
  --light:#eceef1;
  --white:#fff;
}
*{box-sizing:border-box;margin:0;padding:0}
html,body{width:1200px;height:4396px;overflow:hidden}
body{font-family:"Barlow",sans-serif;color:var(--text);background:var(--white);position:relative}
.display{font-family:"Russo One",sans-serif;letter-spacing:2px;text-transform:uppercase}
.abs{position:absolute}
svg.ic{display:inline-block;vertical-align:middle}

/* top bar */
.topbar{position:absolute;left:0;top:0;width:1200px;height:46px;background:var(--ink);color:#fff;font-size:14px}
.topbar .item{position:absolute;top:14px;display:flex;align-items:center;gap:8px}
.topbar .lbl{color:var(--red)}

/* nav */
.nav{position:absolute;top:46px;left:0;width:1200px;height:85px;background:#fff}
.brand{position:absolute;left:111px;top:24px;display:flex;align-items:center;gap:8px;font-family:"Russo One",sans-serif;font-size:18px;color:var(--ink);line-height:1.05;text-transform:uppercase}
.brand .mark{width:14px;height:14px;background:var(--red)}
.nav a{position:absolute;top:34px;font-size:15px;font-weight:500;color:var(--ink);text-decoration:none;display:flex;align-items:center;gap:6px}
.nav a.active{color:var(--red)}
.nav a.active::before{content:"";position:absolute;left:0;right:0;top:-14px;height:2px;background:var(--red)}
.btn{display:flex;align-items:center;justify-content:center;font-weight:700;text-transform:uppercase;color:#fff;background:var(--red)}
.nav .book{position:absolute;left:942px;top:22px;width:145px;height:41px;font-size:16px;border-radius:2px}

/* hero */
.hero{position:absolute;top:131px;left:0;width:1200px;height:629px;background:linear-gradient(90deg,#151826 0%,#262a36 38%,#4b4e58 60%,#7a7b80 80%,#5a5653 100%)}
.hero-text{position:absolute;left:111px;top:78px;color:#fff}
.hero-text .kicker{color:var(--red);font-size:25px}
.hero-text h1{font-size:33px;font-weight:400;margin-top:14px}
.hero-text p{font-size:15px;line-height:31px;margin-top:18px;width:500px}
.booking{position:absolute;left:111px;top:405px;width:476px;height:355px;background:var(--ink)}
.booking h2{position:absolute;left:0;right:0;top:38px;text-align:center;color:#fff;font-size:25px;font-weight:400}
.field{position:absolute;height:49px;background:#fff;font-size:13px;color:#555;display:flex;align-items:center;justify-content:space-between;padding:0 24px}
.booking .go{position:absolute;left:43px;top:308px;width:387px;height:50px;font-size:16px}

/* about */
.about{position:absolute;top:760px;left:0;width:1200px;height:735px;background:linear-gradient(120deg,#f4f5f7,#e4e6ea 55%,#eff0f3)}
.about-name{position:absolute;left:100px;top:150px;height:470px;writing-mode:vertical-rl;transform:rotate(180deg);font-family:"Russo One",sans-serif;font-size:58px;line-height:70px;color:var(--ink);text-transform:uppercase;text-align:center}
.ph{position:absolute}
.about h2{position:absolute;left:628px;top:105px;font-size:30px;color:var(--navy);font-weight:400}
.about h2 span,.section-title span{color:var(--red)}
.about p.lead{position:absolute;left:628px;top:162px;width:500px;font-size:14.5px;line-height:30px;color:#3a3f4a}
.stat{position:absolute;left:628px;width:493px}
.stat .row{display:flex;justify-content:space-between;font-size:15px}
.stat .name{color:var(--red);font-weight:600}
.stat .avail{color:#333}
.stat .avail b{color:var(--red);font-weight:400}
.stat .track{margin-top:20px;height:4px;background:#d3d6dc;position:relative}
.stat .fill{position:absolute;left:0;top:0;height:4px;background:var(--ink)}
.about .more{position:absolute;left:628px;top:605px;width:147px;height:38px;font-size:15px;border-radius:2px}

/* forklifts */
.section-title{position:absolute;left:0;width:1200px;text-align:center;font-size:31px;font-weight:400;color:var(--navy)}
.section-lead{position:absolute;left:0;width:1200px;text-align:center;font-size:15px;line-height:30px;color:#3a3f4a}
.card{position:absolute;width:311px;height:710px;background:#fff;box-shadow:0 4px 14px rgba(13,18,48,.12);display:flex;flex-direction:column}
.card .img{height:231px;position:relative}
.badge{position:absolute;left:4px;top:4px;background:var(--red);color:#fff;font-size:11px;font-weight:600;padding:2px 5px}
.card .links{position:absolute;left:0;right:0;bottom:10px;display:flex;justify-content:center;gap:18px;color:#fff;font-size:13px;font-weight:500}
.card .links i{font-style:normal;opacity:.8}
.card h3{text-align:center;font-size:22px;font-weight:700;color:#111;margin-top:29px}
.price{display:flex;justify-content:space-between;align-items:center;padding:0 26px;margin-top:18px}
.price .t{font-size:14px;font-weight:600;color:#111}
.price .t small{display:block;font-size:12px;font-weight:400;color:var(--muted);margin-top:4px}
.price .v{font-size:28px;font-weight:600;color:var(--navy)}
.rates{display:flex;border-top:1px solid var(--line);border-bottom:1px solid var(--line);margin-top:14px;height:34px}
.rates div{flex:1;display:flex;align-items:center;justify-content:center;font-size:14px;color:#222;border-right:1px solid var(--line)}
.rates div:last-child{border-right:0;flex:1.35}
.rates div:first-child{flex:.85}
.rates b{font-weight:600;margin-left:4px;color:var(--navy)}
.specs{list-style:none;padding-left:52px;margin-top:20px}
.specs li{height:31px;display:flex;align-items:center;gap:14px;font-size:14px;color:#333}
.card .reserve{margin-top:auto;height:41px;font-size:16px;background:var(--navy)}
.card.hot .price .v{color:var(--red)}
.card.hot .rates .wk{background:var(--red);color:#fff}
.card.hot .rates .wk b{color:#fff}
.card.hot .reserve{background:var(--red)}
.card.hot .links i.res{color:var(--red);opacity:1}
.card.hot .rates b.m{color:var(--red)}
.tick{color:var(--navy)}
.card.hot .tick{color:var(--red)}

/* sale */
.sale{position:absolute;top:3281px;left:0;width:1200px;height:625px;background:var(--sale)}
.sale .section-title{color:#fff;top:73px}
.sale .section-lead{color:#fff;top:118px}
.sale-card{position:absolute;top:205px;width:489px;height:266px;background:#fff}
.sale-card .ph{left:14px;top:14px;width:242px;height:238px}
.sale-card .body{position:absolute;left:280px;top:18px;right:10px}
.sale-card h4{font-size:21px;font-weight:700;color:var(--sale)}
.sale-card .t{font-size:14px;font-weight:600;color:#111;margin-top:12px}
.sale-card small{display:block;font-size:12px;color:var(--muted);margin-top:6px}
.sale-card ul{list-style:none;margin-top:8px}
.sale-card li{height:32px;display:flex;align-items:center;gap:12px;font-size:14px;color:#333}
.sale-card .v{font-size:28px;font-weight:600;color:var(--red);margin-top:8px}
.sale-card .buy{position:absolute;left:256px;right:0;bottom:0;height:38px;font-size:16px}
.pager{position:absolute;top:3812px;left:676px;display:flex;gap:11px}
.pager span{width:24px;height:26px;display:flex;align-items:center;justify-content:center;font-size:15px;color:#fff}
.pager span.on{background:var(--red)}
.next{position:absolute;left:1017px;top:3810px;width:98px;height:36px;font-size:15px;font-weight:500;text-transform:none;gap:8px;border-radius:3px}

/* footer */
.footer{position:absolute;top:3906px;left:0;width:1200px;height:490px;background:var(--ink);color:#fff}
.footer .brand{left:111px;top:62px;color:#fff;font-size:20px}
.footer .vr{position:absolute;left:350px;top:58px;width:2px;height:44px;background:#fff}
.footer .news{position:absolute;left:386px;top:64px;font-size:25px;font-weight:500}
.footer .email{position:absolute;left:739px;top:52px;width:191px;height:46px;border:1px solid #fff;font-size:12px;display:flex;align-items:center;padding-left:12px}
.footer .sub{position:absolute;left:940px;top:52px;width:159px;height:46px;font-size:16px;gap:10px}
.footer .hr{position:absolute;left:111px;right:101px;height:1px;background:#3b405c}
.footer h5{position:absolute;top:180px;font-family:"Russo One",sans-serif;font-weight:400;font-size:23px;letter-spacing:2px}
.footer p.about-f{position:absolute;left:113px;top:240px;width:290px;font-size:14px;line-height:31px}
.footer ul{position:absolute;top:240px;list-style:none;font-size:15px;line-height:34px}
.footer ul.contact li{display:flex;gap:14px;align-items:flex-start;line-height:28px;margin-bottom:12px}
.socials{position:absolute;left:113px;top:444px;display:flex;gap:6px}
.socials span{width:26px;height:26px;border:1.5px solid #fff;border-radius:50%}
.copy{position:absolute;right:112px;top:452px;font-size:14px}
</style>
</head>
<body>
<svg width="0" height="0" style="position:absolute">
  <symbol id="tick" viewBox="0 0 16 16"><circle cx="8" cy="8" r="8" fill="currentColor"/><path d="M4.5 8.2l2.3 2.3 4.7-4.8" stroke="#fff" stroke-width="1.8" fill="none"/></symbol>
  <symbol id="chev" viewBox="0 0 10 6"><path d="M1 1l4 4 4-4" stroke="currentColor" stroke-width="1.5" fill="none"/></symbol>
  <symbol id="cal" viewBox="0 0 12 12"><rect x="1" y="2" width="10" height="9" fill="none" stroke="#444"/><path d="M1 5h10M4 2v9M8 2v9M1 8h10" stroke="#444"/></symbol>
  <symbol id="pin" viewBox="0 0 12 16"><path d="M6 0a6 6 0 0 0-6 6c0 4.5 6 10 6 10s6-5.5 6-10a6 6 0 0 0-6-6z" fill="currentColor"/><circle cx="6" cy="6" r="2.2" fill="var(--ink)"/></symbol>
  <symbol id="mail" viewBox="0 0 16 12"><rect x="1" y="1" width="14" height="10" fill="none" stroke="currentColor" stroke-width="1.5"/><path d="M1 1l7 6 7-6" fill="none" stroke="currentColor" stroke-width="1.5"/></symbol>
  <symbol id="clock" viewBox="0 0 16 16"><circle cx="8" cy="8" r="7" fill="none" stroke="currentColor" stroke-width="1.5"/><path d="M8 4v4l3 2" fill="none" stroke="currentColor" stroke-width="1.5"/></symbol>
  <symbol id="phone" viewBox="0 0 16 16"><path d="M3 1l3 0 1.5 4-2 1.5a9 9 0 0 0 4 4L11 8.5l4 1.5v3a2 2 0 0 1-2 2C7 15 1 9 1 3a2 2 0 0 1 2-2z" fill="currentColor"/></symbol>
  <symbol id="arrow" viewBox="0 0 16 12"><path d="M1 6h13M9 1l5 5-5 5" stroke="currentColor" stroke-width="2" fill="none"/></symbol>
</svg>

<header class="topbar">
  <div class="item" style="left:111px"><svg class="ic" width="11" height="15" style="color:var(--red)"><use href="#pin"/></svg><span class="lbl">Location :</span> United States, Brightmore Machinery</div>
  <div class="item" style="left:526px"><svg class="ic" width="15" height="12" style="color:var(--red)"><use href="#mail"/></svg><span class="lbl">E-mail :</span> hello@brightmore-mach.com</div>
  <div class="item" style="left:823px"><svg class="ic" width="15" height="15" style="color:var(--red)"><use href="#clock"/></svg><span class="lbl">Open Hours :</span> Fri: 8:00 am - 7:00 pm</div>
</header>

<nav class="nav">
  <div class="brand"><span class="mark"></span>Brightmore<br>Machinery</div>
  <a class="active" style="left:318px">Home</a>
  <a style="left:411px">Company <svg class="ic" width="10" height="6"><use href="#chev"/></svg></a>
  <a style="left:522px">Our Services <svg class="ic" width="10" height="6"><use href="#chev"/></svg></a>
  <a style="left:655px">Latest News</a>
  <a style="left:763px">Rental <svg class="ic" width="10" height="6"><use href="#chev"/></svg></a>
  <a style="left:855px">Sale <svg class="ic" width="10" height="6"><use href="#chev"/></svg></a>
  <div class="btn book">Book Now</div>
</nav>

<section class="hero" role="img" aria-label="Warehouse interior with a red reach truck forklift parked by a wall">
  <div class="hero-text">
    <div class="kicker display">Welcome to</div>
    <h1 class="display">Brightmore Machinery</h1>
    <p>Lorem ipsum dolor sit amet, consectetur adipiscing elit, sed do eiusmod tempor incididunt ut labore et dolore magna aliqua.</p>
  </div>
</section>
<svg class="abs" style="left:68px;top:759px" width="560" height="41"><polygon points="0,0 560,0 519,41 43,41" fill="#0d1230"/></svg>
<div class="booking">
  <h2 class="display">Book Now For Rent</h2>
  <div class="field" style="left:43px;top:104px;width:387px">What are you looking for ? <svg class="ic" width="10" height="6"><use href="#chev"/></svg></div>
  <div class="field" style="left:43px;top:172px;width:387px">Select Category ? <svg class="ic" width="10" height="6"><use href="#chev"/></svg></div>
  <div class="field" style="left:43px;top:240px;width:186px;padding:0 16px">DD / MM / YYYY <svg class="ic" width="12" height="12"><use href="#cal"/></svg></div>
  <div class="field" style="left:244px;top:240px;width:186px;padding:0 16px">DD / MM / YYYY <svg class="ic" width="12" height="12"><use href="#cal"/></svg></div>
  <div class="btn go">Book Now</div>
</div>

<section class="about">
  <div class="about-name">Brightmore<br>Machinery</div>
  <div class="ph" role="img" aria-label="Red and black order picker forklift with raised mast" style="left:316px;top:76px;width:205px;height:606px;background:linear-gradient(180deg,#2a2d35 0%,#3a3d45 55%,#c3202a 62%,#b71c24 90%,#1b1c20 100%)"></div>
  <h2 class="display">About <span>Us</span></h2>
  <p class="lead">Lorem ipsum dolor sit amet, consectetur adipiscing elit, sed do eiusmod tempor incididunt ut labore et dolore magna aliqua. Ut enim ad minim veniam,quis nostrud exercitation ullamco laboris nisi ut aliquip ex ea commodo consequat.</p>
  <div class="stat" style="top:303px"><div class="row"><span class="name">Electric forklifts</span><span class="avail">(Available)<b>18</b>/20</span></div><div class="track"><div class="fill" style="width:90%"></div></div></div>
  <div class="stat" style="top:375px"><div class="row"><span class="name">Reach trucks</span><span class="avail">(Available)<b>14</b>/20</span></div><div class="track"><div class="fill" style="width:72%"></div></div></div>
  <div class="stat" style="top:447px"><div class="row"><span class="name">Order pickers</span><span class="avail">(Available)<b>10</b>/20</span></div><div class="track"><div class="fill" style="width:61%"></div></div></div>
  <div class="stat" style="top:519px"><div class="row"><span class="name">Swing reach</span><span class="avail">(Available)<b>08</b>/20</span></div><div class="track"><div class="fill" style="width:36%"></div></div></div>
  <div class="btn more">Learn More</div>
</section>

<h2 class="section-title display" style="top:1556px">Our <span>Forklifts</span></h2>
<p class="section-lead" style="top:1613px">Lorem ipsum dolor sit amet, consectetur adipiscing elit, sed do eiusmod tempor incididunt ut labore et dolore magna aliqua.<br>Ut enim ad minim veniam,quis nostrud exercitation ullamco laboris nisi ut aliquip ex ea commodo consequat.<br>Duis aute irure dolor in reprehenderit in voluptate velit esse cillum dolore eu fugiat nulla pariatur.</p>

<!-- row 1 -->
<article class="card" style="left:94px;top:1741px">
  <div class="img" role="img" aria-label="Row of electric forklifts in a warehouse" style="background:linear-gradient(180deg,#9aa0a6,#5b6068 60%,#2b2e34)"><span class="badge">20% OFF</span><div class="links"><span>View Details</span><i>|</i><span>Reserve now</span></div></div>
  <h3>Electric forklifts</h3>
  <div class="price"><div class="t">Total Rental Price<small>Incl. taxes</small></div><div class="v">$525</div></div>
  <div class="rates"><div>$110 /<b>Day</b></div><div class="wk">$525 /<b>Week</b></div><div>$2,100 /<b class="m">Month</b></div></div>
  <ul class="specs"><li><svg class="ic tick" width="16" height="16"><use href="#tick"/></svg>Maximum Reach: 5Meter</li><li><svg class="ic tick" width="16" height="16"><use href="#tick"/></svg>Operating Weight: 0.8Ton</li><li><svg class="ic tick" width="16" height="16"><use href="#tick"/></svg>Model: Mini MD45</li><li><svg class="ic tick" width="16" height="16"><use href="#tick"/></svg>Digging Depth: 3.3Meter</li><li><svg class="ic tick" width="16" height="16"><use href="#tick"/></svg>Manufacture Year: 2015</li><li><svg class="ic tick" width="16" height="16"><use href="#tick"/></svg>Brand: Torvik Dyne</li><li><svg class="ic tick" width="16" height="16"><use href="#tick"/></svg>Walking Speed: 2.7km/h</li></ul>
  <div class="btn reserve">Reserve Now</div>
</article>
<article class="card hot" style="left:444px;top:1741px">
  <div class="img" role="img" aria-label="Red forklift in a dim warehouse with orange lights" style="background:radial-gradient(circle at 50% 55%,#b8452d,#4a2420 55%,#1c1414)"><span class="badge">20% OFF</span><div class="links"><span>View Details</span><i>|</i><i class="res">Reserve now</i></div></div>
  <h3>Reach trucks</h3>
  <div class="price"><div class="t">Total Rental Price<small>Incl. taxes</small></div><div class="v">$525</div></div>
  <div class="rates"><div>$110 /<b>Day</b></div><div class="wk">$525 /<b>Week</b></div><div>$2,100 /<b class="m">Month</b></div></div>
  <ul class="specs"><li><svg class="ic tick" width="16" height="16"><use href="#tick"/></svg>Maximum Reach: 5Meter</li><li><svg class="ic tick" width="16" height="16"><use href="#tick"/></svg>Operating Weight: 0.8Ton</li><li><svg class="ic tick" width="16" height="16"><use href="#tick"/></svg>Model: Mini MD45</li><li><svg class="ic tick" width="16" height="16"><use href="#tick"/></svg>Digging Depth: 3.3Meter</li><li><svg class="ic tick" width="16" height="16"><use href="#tick"/></svg>Manufacture Year: 2015</li><li><svg class="ic tick" width="16" height="16"><use href="#tick"/></svg>Brand: Torvik Dyne</li><li><svg class="ic tick" width="16" height="16"><use href="#tick"/></svg>Walking Speed: 2.7km/h</li></ul>
  <div class="btn reserve">Reserve Now</div>
</article>
<article class="card" style="left:794px;top:1741px">
  <div class="img" role="img" aria-label="Yellow order picker among tall warehouse racks" style="background:linear-gradient(120deg,#c9a331 0%,#6c7080 35%,#8a8f9c 70%,#4c5060)"><span class="badge">20% OFF</span><div class="links"><span>View Details</span><i>|</i><span>Reserve now</span></div></div>
  <h3>Order pickers</h3>
  <div class="price"><div class="t">Total Rental Price<small>Incl. taxes</small></div><div class="v">$525</div></div>
  <div class="rates"><div>$110 /<b>Day</b></div><div class="wk">$525 /<b>Week</b></div><div>$2,100 /<b class="m">Month</b></div></div>
  <ul class="specs"><li><svg class="ic tick" width="16" height="16"><use href="#tick"/></svg>Maximum Reach: 5Meter</li><li><svg class="ic tick" width="16" height="16"><use href="#tick"/></svg>Operating Weight: 0.8Ton</li><li><svg class="ic tick" width="16" height="16"><use href="#tick"/></svg>Model: Mini MD45</li><li><svg class="ic tick" width="16" height="16"><use href="#tick"/></svg>Digging Depth: 3.3Meter</li><li><svg class="ic tick" width="16" height="16"><use href="#tick"/></svg>Manufacture Year: 2015</li><li><svg class="ic tick" width="16" height="16"><use href="#tick"/></svg>Brand: Torvik Dyne</li><li><svg class="ic tick" width="16" height="16"><use href="#tick"/></svg>Walking Speed: 2.7km/h</li></ul>
  <div class="btn reserve">Reserve Now</div>
</article>

<!-- row 2 -->
<article class="card" style="left:91px;top:2494px">
  <div class="img" role="img" aria-label="Red counterbalance forklifts parked in a warehouse" style="background:linear-gradient(180deg,#8c8f95,#4d4f55 50%,#6b2a2e 75%,#2a2b30)"><span class="badge">20% OFF</span><div class="links"><span>View Details</span><i>|</i><span>Reserve now</span></div></div>
  <h3>Counterbalances</h3>
  <div class="price"><div class="t">Total Rental Price<small>Incl. taxes</small></div><div class="v">$525</div></div>
  <div class="rates"><div>$110 /<b>Day</b></div><div class="wk">$525 /<b>Week</b></div><div>$2,100 /<b class="m">Month</b></div></div>
  <ul class="specs"><li><svg class="ic tick" width="16" height="16"><use href="#tick"/></svg>Maximum Reach: 5Meter</li><li><svg class="ic tick" width="16" height="16"><use href="#tick"/></svg>Operating Weight: 0.8Ton</li><li><svg class="ic tick" width="16" height="16"><use href="#tick"/></svg>Model: Mini MD45</li><li><svg class="ic tick" width="16" height="16"><use href="#tick"/></svg>Digging Depth: 3.3Meter</li><li><svg class="ic tick" width="16" height="16"><use href="#tick"/></svg>Manufacture Year: 2015</li><li><svg class="ic tick" width="16" height="16"><use href="#tick"/></svg>Brand: Torvik Dyne</li><li><svg class="ic tick" width="16" height="16"><use href="#tick"/></svg>Walking Speed: 2.7km/h</li></ul>
  <div class="btn reserve">Reserve Now</div>
</article>
<article class="card" style="left:444px;top:2494px">
  <div class="img" role="img" aria-label="Red and black swing reach forklift in a warehouse" style="background:linear-gradient(180deg,#7d8088,#45474e 50%,#7a2327 78%,#27282d)"><span class="badge">20% OFF</span><div class="links"><span>View Details</span><i>|</i><span>Reserve now</span></div></div>
  <h3>Swing reach</h3>
  <div class="price"><div class="t">Total Rental Price<small>Incl. taxes</small></div><div class="v">$525</div></div>
  <div class="rates"><div>$110 /<b>Day</b></div><div class="wk">$525 /<b>Week</b></div><div>$2,100 /<b class="m">Month</b></div></div>
  <ul class="specs"><li><svg class="ic tick" width="16" height="16"><use href="#tick"/></svg>Maximum Reach: 5Meter</li><li><svg class="ic tick" width="16" height="16"><use href="#tick"/></svg>Operating Weight: 0.8Ton</li><li><svg class="ic tick" width="16" height="16"><use href="#tick"/></svg>Model: Mini MD45</li><li><svg class="ic tick" width="16" height="16"><use href="#tick"/></svg>Digging Depth: 3.3Meter</li><li><svg class="ic tick" width="16" height="16"><use href="#tick"/></svg>Manufacture Year: 2015</li><li><svg class="ic tick" width="16" height="16"><use href="#tick"/></svg>Brand: Torvik Dyne</li><li><svg class="ic tick" width="16" height="16"><use href="#tick"/></svg>Walking Speed: 2.7km/h</li></ul>
  <div class="btn reserve">Reserve Now</div>
</article>
<article class="card" style="left:794px;top:2494px">
  <div class="img" role="img" aria-label="Propane sit down forklift by a warehouse wall" style="background:linear-gradient(180deg,#8a8c90,#55575c 50%,#6e2529 80%,#2a2b2f)"><span class="badge">20% OFF</span><div class="links"><span>View Details</span><i>|</i><span>Reserve now</span></div></div>
  <h3>Propane sit down</h3>
  <div class="price"><div class="t">Total Rental Price<small>Incl. taxes</small></div><div class="v">$525</div></div>
  <div class="rates"><div>$110 /<b>Day</b></div><div class="wk">$525 /<b>Week</b></div><div>$2,100 /<b class="m">Month</b></div></div>
  <ul class="specs"><li><svg class="ic tick" width="16" height="16"><use href="#tick"/></svg>Maximum Reach: 5Meter</li><li><svg class="ic tick" width="16" height="16"><use href="#tick"/></svg>Operating Weight: 0.8Ton</li><li><svg class="ic tick" width="16" height="16"><use href="#tick"/></svg>Model: Mini MD45</li><li><svg class="ic tick" width="16" height="16"><use href="#tick"/></svg>Digging Depth: 3.3Meter</li><li><svg class="ic tick" width="16" height="16"><use href="#tick"/></svg>Manufacture Year: 2015</li><li><svg class="ic tick" width="16" height="16"><use href="#tick"/></svg>Brand: Torvik Dyne</li><li><svg class="ic tick" width="16" height="16"><use href="#tick"/></svg>Walking Speed: 2.7km/h</li></ul>
  <div class="btn reserve">Reserve Now</div>
</article>

<section class="sale">
  <h2 class="section-title display">Forklifts For Sale</h2>
  <p class="section-lead">Lorem ipsum dolor sit amet, consectetur adipiscing elit, sed do eiusmod tempor incididunt ut labore et dolore magna aliqua.<br>Ut enim ad minim veniam.</p>
  <article class="sale-card" style="left:85px">
    <div class="ph" role="img" aria-label="Counterbalance forklift for sale in a warehouse" style="background:linear-gradient(180deg,#8e9197,#55575d 55%,#6c2428 80%,#3a3b40)"></div>
    <div class="body">
      <h4>Counterbalances</h4>
      <div class="t">Total Sale Price</div><small>Incl. taxes</small>
      <ul><li><svg class="ic tick" width="16" height="16"><use href="#tick"/></svg>Maximum Reach: 5Meter</li><li><svg class="ic tick" width="16" height="16"><use href="#tick"/></svg>Operating Weight: 0.8Ton</li></ul>
      <div class="v">$5250</div>
    </div>
    <div class="btn buy">Reserve Now</div>
  </article>
  <article class="sale-card" style="left:626px">
    <div class="ph" role="img" aria-label="Red counterbalance forklift for sale on a warehouse floor" style="background:linear-gradient(180deg,#a3a5aa,#6a6c71 50%,#8a2529 75%,#45464b)"></div>
    <div class="body">
      <h4>Counterbalances</h4>
      <div class="t">Total Sale Price</div><small>Incl. taxes</small>
      <ul><li><svg class="ic tick" width="16" height="16"><use href="#tick"/></svg>Maximum Reach: 5Meter</li><li><svg class="ic tick" width="16" height="16"><use href="#tick"/></svg>Operating Weight: 0.8Ton</li></ul>
      <div class="v">$5250</div>
    </div>
    <div class="btn buy">Reserve Now</div>
  </article>
</section>
<div class="pager"><span class="on">1</span><span>2</span><span>3</span><span>4</span><span>5</span><span>6</span><span>7</span><span>8</span><span>9</span></div>
<div class="btn next">Next <svg class="ic" width="6" height="10" viewBox="0 0 6 10"><path d="M1 1l4 4-4 4" stroke="#fff" stroke-width="1.5" fill="none"/></svg></div>

<footer class="footer">
  <div class="brand"><span class="mark"></span>Brightmore<br>Machinery</div>
  <div class="vr"></div>
  <div class="news">Newsletter Subscription</div>
  <div class="email">Enter Your E-mail</div>
  <div class="btn sub">Subscribe <svg class="ic" width="16" height="12"><use href="#arrow"/></svg></div>
  <div class="hr" style="top:139px"></div>
  <h5 style="left:113px">About Us</h5>
  <h5 style="left:449px">Quick Links</h5>
  <h5 style="left:679px">About Info</h5>
  <h5 style="left:891px">Contact Us</h5>
  <p class="about-f">Lorem ipsum dolor sit amet, consectetur adipiscing elit, sed do eiusmod tempor incid-idunt ut labore et dolore magna aliqua. Ut enim ad minim veniam, quis nostrud exer-citation ullamco laboris.</p>
  <ul style="left:449px"><li>Terms of Service</li><li>Privacy Policy</li><li>Returns Policy</li><li>Our Locations</li><li>Contact Us</li></ul>
  <ul style="left:679px"><li>Home</li><li>Company</li><li>Services</li><li>Rental</li><li>Sale</li></ul>
  <ul class="contact" style="left:891px;width:220px">
    <li><svg class="ic" width="12" height="16" style="color:#fff;margin-top:6px;flex:none"><use href="#pin"/></svg><span>United States, Brightmore Machinery</span></li>
    <li><svg class="ic" width="14" height="14" style="color:#fff;margin-top:7px;flex:none"><use href="#phone"/></svg><span>+1 555 014 2290</span></li>
    <li><svg class="ic" width="15" height="12" style="color:#fff;margin-top:8px;flex:none"><use href="#mail"/></svg><span>hello@brightmore-mach.com</span></li>
  </ul>
  <div class="hr" style="top:432px"></div>
  <div class="socials"><span></span><span></span><span></span><span></span><span></span></div>
  <div class="copy">Copyright © 2024 Brightmore Machinery. All rights reserved.</div>
</footer>
</body>
</html>
```